Architectural Design Build company needs a direct mail flyer

We are a fully service Design Build company who specialize in luxury custom and pre-designed new homes and major home renovations. Our team consists of seasoned architectural, interior design and general contracting professionals all under one roof. We offer clients a transparent, streamlined process to maximize their investment and completion on a timely basis. Leveraging photography and a few before and after and also our Best Builder Awards.

Target Market(s)

Homeowners and buyers between 40-60 years old and financial investment of $300k or more for renovations and $1,000,000 or more for new construction.

Industry/Entity Type

homebuilding and renovations

Colors

Designer to choose colors to be used in the design.

Requirements
Must have
• The construction segments we are focusing this mailer on are transformative renovations and professionally designed custom new homes. . Should have the Pelbrook Before kitchen and after as well as the exterior before and after. and new construction elevation photos.
Nice to have
• WOuld like to see two befores and afters highlighted, mention that are architect and designer are part of the team from start to finish,

```html
<!DOCTYPE html>
<html lang="en">
<head>
<meta charset="utf-8">
<title>Ardson Design Build — Direct Mail Flyer</title>
<link href="https://fonts.googleapis.com/css2?family=Poppins:wght@400;500;600;700;800&family=Montserrat:wght@400;500&display=swap" rel="stylesheet">
<style>
:root{
  --lime:#d9e36a;
  --olive:#b4bd4f;
  --ink:#1f1f1f;
  --dark:#242424;
  --paper:#ffffff;
  --mist:#f1f1f0;
  --stage:#6b6c6f;
  --soft:#e4e4e4;
}
*{margin:0;padding:0;box-sizing:border-box}
html,body{width:1200px;height:866px;overflow:hidden;background:var(--stage)}
body{position:relative;font-family:"Montserrat",sans-serif;color:var(--ink)}
.sheet{position:absolute;top:75px;width:512px;height:717px;background:var(--paper);overflow:hidden;box-shadow:0 6px 18px rgba(0,0,0,.35)}
.sheet--front{left:72px}
.sheet--back{left:617px;background:var(--mist)}
.abs{position:absolute}
.shape{position:absolute;left:0;top:0}
.head{font-family:"Poppins",sans-serif;font-weight:700;line-height:1;text-transform:uppercase;white-space:nowrap}
.just{text-align:justify}

/* shared */
.site{position:absolute;font-family:"Poppins",sans-serif;font-weight:500;font-size:9.5px;letter-spacing:1.7px;white-space:nowrap}
.info{position:absolute;font-family:"Poppins",sans-serif;white-space:nowrap}
.info__label{font-weight:500;line-height:1}
.info__phone{font-weight:700;line-height:1.1}
.info__lic{font-weight:700;font-size:6.5px}
.mail{position:absolute;display:flex;align-items:center;gap:6px;font-family:"Poppins",sans-serif;font-size:12px;white-space:nowrap}

/* front */
.brand{left:23px;top:22px;display:flex;align-items:center;gap:8px}
.brand__mark{width:11px;height:11px;background:var(--ink)}
.brand__name{font-family:"Poppins",sans-serif;font-weight:800;font-size:30px;letter-spacing:1px;line-height:1}
.brand__tag{font-family:"Poppins",sans-serif;font-weight:700;font-size:10.5px;letter-spacing:2px;margin-left:8px}
.hero-photo{left:0;top:71px;width:512px;height:258px;background:linear-gradient(160deg,#6f7f4e 0%,#d6d9d7 30%,#f2f2ef 55%,#9a9c96 80%,#5b5d57 100%)}
.hero__kicker{left:24px;top:171px;font-family:"Poppins",sans-serif;font-weight:500;font-size:10.5px;line-height:13.5px}
.hero__l1{left:24px;top:200px;font-size:20px}
.hero__l2{left:24px;top:222px;font-size:33px;font-weight:800}
.hero__l3{left:24px;top:257px;font-size:21px}
.hero__l4{left:24px;top:283px;font-size:21px;display:flex;align-items:center;gap:5px}
.hero__l4 span{display:block;width:66px;height:2px;background:var(--ink)}
.hero__copy{left:24px;top:309px;width:196px;font-size:7px;line-height:9px}
.banner{left:312px;top:336px;font-size:13px;line-height:17.3px}
.services__title{left:24px;top:365px;font-size:17px}
.rule{position:absolute;height:3px}
.services__copy{left:24px;top:393px;width:214px;font-size:7.1px;line-height:9px}
.svc{position:absolute;left:26px;display:flex;gap:5px}
.svc__icon{flex:none;width:25px;height:27px;margin-top:2px}
.svc__text{width:187px}
.svc h3,.val h3{font-family:"Poppins",sans-serif;font-weight:700;font-size:8px;color:var(--lime);line-height:10px;white-space:nowrap}
.svc p{font-size:6.3px;line-height:8.7px;color:var(--soft);text-align:justify}
.welcome{left:284px;top:403px;font-size:17.5px;color:#fff}
.welcome em{font-style:normal;color:var(--lime)}
.welcome__copy{left:284px;top:436px;width:206px;color:var(--soft);font-size:6.4px;line-height:9px}
.val{position:absolute;left:280px;display:flex;gap:1px}
.val__icon{flex:none;width:15px;height:16px;margin-top:4px}
.val__text{width:182px}
.val p{font-size:6.1px;line-height:7.6px;color:var(--soft);text-align:justify}

/* back */
.about__title{left:24px;top:19px;font-size:25px;font-weight:800;color:var(--lime)}
.about__copy{left:20px;top:54px;width:226px;color:#f0f0f0;font-size:7.8px;line-height:10.8px}
.about__copy p+p{margin-top:10.8px}
.team-photo{left:228px;top:43px;width:284px;height:189px;background:linear-gradient(180deg,#d9e36a 0%,#c9cf6a 40%,#3a3a36 75%,#222 100%);clip-path:polygon(66px 0,100% 0,100% 100%,0 100%)}
.ba{position:absolute;width:103px;height:128px;border:3px solid var(--lime)}
.ba__photo{width:100%;height:100%}
.ba__tag{position:absolute;bottom:-3px;left:50%;transform:translateX(-50%);background:var(--lime);font-family:"Poppins",sans-serif;font-weight:600;font-size:8px;line-height:13px;padding:0 8px}
.resilient{left:253px;top:244px;font-size:19.5px;line-height:24px}
.resilient__copy{left:253px;top:293px;width:234px;font-size:6.6px;line-height:10.8px;color:#333}
.resilient__copy p+p{margin-top:8.5px}
.award{position:absolute;top:444px;height:92px}
.promise{left:21px;top:525px;font-size:15.5px;line-height:20px}
.quote{position:absolute;left:270px;top:574px;width:224px;text-align:center;font-family:"Poppins",sans-serif;font-size:12.5px;line-height:15.5px}
.client{position:absolute;left:264px;top:653px}
.client__name{font-family:"Poppins",sans-serif;font-weight:700;font-size:13px;line-height:16px;color:var(--lime);letter-spacing:.6px}
.client__role{font-family:"Poppins",sans-serif;font-size:9px;line-height:12px;display:flex;align-items:center;gap:6px}
.client__role span{display:block;width:132px;height:1.5px;background:var(--lime)}
</style>
</head>
<body>

<!-- FRONT -->
<section class="sheet sheet--front">
  <div class="abs brand"><span class="brand__mark"></span><span class="brand__name">ARDSON</span><span class="brand__tag">DESIGN BUILD</span></div>
  <div class="site" style="right:23px;top:32px">www.ardsonbuild.com</div>

  <div class="abs hero-photo" role="img" aria-label="Photo of a white two-storey custom home with a front porch"></div>

  <svg class="shape" width="512" height="717" viewBox="0 0 512 717">
    <polygon points="0,143 169,143 263,359 0,359" fill="var(--lime)"/>
    <polygon points="300,328 512,328 512,391 279,391" fill="var(--lime)"/>
    <polygon points="263,359 279,391 266,359" fill="var(--olive)"/>
    <polygon points="266,359 279,391 512,391 512,629 0,629 0,443 250,443" fill="var(--dark)"/>
    <polygon points="0,359 266,359 250,443 0,443" fill="var(--paper)"/>
    <rect x="0" y="443" width="270" height="214" fill="var(--dark)"/>
    <polygon points="280,629 512,629 512,717 212,717" fill="var(--lime)"/>
  </svg>

  <div class="abs hero__kicker">LUXURY<br>CUSTOM HOMES</div>
  <div class="abs head hero__l1">BUILDING</div>
  <div class="abs head hero__l2">DREAMS</div>
  <div class="abs head hero__l3">TRANSFORMING</div>
  <div class="abs head hero__l4">LIVES <span></span></div>
  <p class="abs hero__copy">Our expertise has created some exciting opportunities for commercial work. Together, we can help your dream venture come to life by creating unforgettable spaces for your clientele.</p>

  <div class="abs head banner">Building exceptional<br>luxury homes tailored<br>to your unique vision</div>

  <h2 class="abs head services__title">OUR SERVICES</h2>
  <div class="rule" style="left:24px;top:386px;width:52px;background:var(--lime)"></div>
  <p class="abs services__copy">At Ardson, one of the best luxury home builders, we are dedicated to creating custom luxury homes that perfectly align with your unique vision. With meticulous attention to detail and a commitment to quality craftsmanship, we transform your dreams into reality</p>

  <div class="svc" style="top:456px">
    <svg class="svc__icon" viewBox="0 0 26 28"><polygon points="13,1 25,7.5 25,20.5 13,27 1,20.5 1,7.5" fill="var(--lime)"/><rect x="9" y="8" width="8" height="12" fill="none" stroke="var(--ink)" stroke-width="1.4"/><path d="M11 11h1M14 11h1M11 14h1M14 14h1" stroke="var(--ink)" stroke-width="1.4"/></svg>
    <div class="svc__text"><h3>BUILDING DREAMS</h3><p>Our clients are not just investing in structures, but in their dreams, aspirations, and legacies. Ardson specializes in new home builds, transformative renovations, and select commercial ventures.</p></div>
  </div>
  <div class="svc" style="top:519px">
    <svg class="svc__icon" viewBox="0 0 26 28"><polygon points="13,1 25,7.5 25,20.5 13,27 1,20.5 1,7.5" fill="var(--lime)"/><path d="M8 9l10 10M18 9L8 19" stroke="var(--ink)" stroke-width="2.2" stroke-linecap="round"/></svg>
    <div class="svc__text"><h3>TRANSFORMING LIVES</h3><p>We create spaces that not only reflect our clients' unique lifestyles but also foster a sense of belonging and connection. Whether you're blazing a new trail or reimagining the old, we're ready to collaborate every step of the way.</p></div>
  </div>
  <div class="svc" style="top:590px">
    <svg class="svc__icon" viewBox="0 0 26 28"><polygon points="13,1 25,7.5 25,20.5 13,27 1,20.5 1,7.5" fill="var(--lime)"/><rect x="8" y="9" width="10" height="10" rx="1.5" fill="none" stroke="var(--ink)" stroke-width="1.6"/></svg>
    <div class="svc__text"><h3>NEVER THE SAME THING TWICE</h3><p>From the unconventional to the ambitious, we embrace a no-limits attitude—building whatever our clients can imagine, and then some. From sleek modern marvels to historic restorations with a contemporary twist, our portfolio is as diverse as the clients we serve.</p></div>
  </div>

  <h2 class="abs head welcome">WELCOME <em>TO ARDSON</em></h2>
  <div class="rule" style="left:284px;top:429px;width:50px;background:#fff"></div>
  <p class="abs welcome__copy">create a cohesive vision for your home. If you have chosen an architect outside Ardson, we are happy to work alongside your chosen team seamlessly.</p>

  <div class="val" style="top:472px">
    <svg class="val__icon" viewBox="0 0 16 17"><polygon points="8,0.5 15.5,4.5 15.5,12.5 8,16.5 0.5,12.5 0.5,4.5" fill="var(--lime)"/><path d="M4.5 8.6l2.4 2.4 4.6-4.8" fill="none" stroke="var(--ink)" stroke-width="1.6"/></svg>
    <div class="val__text"><h3>FINANCIAL TRANSPARENCY</h3><p>We believe in complete transparency throughout our process, ensuring you're fully informed about every aspect, including design, budget, and schedule.</p></div>
  </div>
  <div class="val" style="top:518px">
    <svg class="val__icon" viewBox="0 0 16 17"><polygon points="8,0.5 15.5,4.5 15.5,12.5 8,16.5 0.5,12.5 0.5,4.5" fill="var(--lime)"/><path d="M4.5 8.6l2.4 2.4 4.6-4.8" fill="none" stroke="var(--ink)" stroke-width="1.6"/></svg>
    <div class="val__text"><h3>RELATIONAL PARTNER</h3><p>We prioritize building strong, cooperative relationships founded on trust, open communication, and shared goals. Our commitment goes beyond simple transactions or contractual obligations, fostering long-term partnerships.</p></div>
  </div>
  <div class="val" style="top:579px">
    <svg class="val__icon" viewBox="0 0 16 17"><polygon points="8,0.5 15.5,4.5 15.5,12.5 8,16.5 0.5,12.5 0.5,4.5" fill="var(--lime)"/><path d="M4.5 8.6l2.4 2.4 4.6-4.8" fill="none" stroke="var(--ink)" stroke-width="1.6"/></svg>
    <div class="val__text"><h3>QUALITY</h3><p>We are dedicated to excellence in every aspect of our work. This means superior craftsmanship, the use of high-caliber materials, and a team of skilled professionals committed to reliability and profession-</p></div>
  </div>

  <svg class="abs" style="left:266px;top:645px" width="39" height="41" viewBox="0 0 40 42"><polygon points="20,1 38,11 38,31 20,41 2,31 2,11" fill="var(--ink)"/><rect x="13" y="12" width="14" height="18" rx="2" fill="none" stroke="var(--lime)" stroke-width="2"/><circle cx="20" cy="19" r="2.6" fill="var(--lime)"/><path d="M15.5 26c1.5-3 7.5-3 9 0" stroke="var(--lime)" stroke-width="1.8" fill="none"/></svg>
  <div class="info" style="left:314px;top:641px">
    <div class="info__label" style="font-size:18.5px">For more info</div>
    <div class="info__phone" style="font-size:24px">555-014-2290</div>
    <div class="info__lic" style="margin-left:2px">CGC #1048221</div>
  </div>

  <div class="mail" style="left:34px;top:676px">
    <svg width="11" height="11" viewBox="0 0 12 12"><path d="M11.5 0.5L0.5 5l4 1.5L6 11z" fill="var(--lime)"/></svg>
    hello@ardsonbuild.com
  </div>
</section>

<!-- BACK -->
<section class="sheet sheet--back">
  <svg class="shape" width="512" height="717" viewBox="0 0 512 717">
    <polygon points="0,0 512,0 512,232 0,232" fill="var(--dark)"/>
    <polygon points="336,0 512,0 512,43 323,43" fill="var(--paper)"/>
    <polygon points="293,43 512,43 512,232 227,232" fill="var(--lime)"/>
    <polygon points="272,496 285,496 238,591 225,591" fill="var(--lime)"/>
    <polygon points="0,591 246,591 230,664 0,664" fill="var(--dark)"/>
    <polygon points="0,664 230,664 214,717 0,717" fill="var(--lime)"/>
    <polygon points="225,694 512,694 512,717 214,717" fill="var(--ink)"/>
  </svg>

  <div class="site" style="right:24px;top:18px">www.ardsonbuild.com</div>
  <h2 class="abs head about__title">ABOUT US</h2>
  <div class="abs about__copy">
    <p>At Ardson, our success is driven by the exceptional talent and dedication of our team. Led by owners Dane Pelbrook, M. Eng., and Miles Orwin- both esteemed former pro football players- our diverse team brings together a wealth of experience and expertise.</p>
    <p>As a design/build company, Ardson seamlessly integrates design and construction services. This collaborative model ensures transparent communication, streamlined workflows, and efficient problem solving throughout the project lifecycle. Clients benefit from a holistic and cohesive approach to their project, resulting in superior quality cost-effectiveness, and timely delivery.</p>
  </div>
  <div class="abs team-photo" role="img" aria-label="Photo of the two company owners standing with arms crossed"></div>

  <div class="ba" style="left:20px;top:246px"><div class="ba__photo" role="img" aria-label="Kitchen before renovation with dark wood cabinets" style="background:linear-gradient(180deg,#6a4030,#4a2c22 60%,#8a8a86)"></div><span class="ba__tag">Before</span></div>
  <div class="ba" style="left:133px;top:246px"><div class="ba__photo" role="img" aria-label="Kitchen after renovation with white cabinets and island" style="background:linear-gradient(180deg,#f4f4f2,#d9d9d6 60%,#6e5a48)"></div><span class="ba__tag">After</span></div>
  <div class="ba" style="left:20px;top:385px"><div class="ba__photo" role="img" aria-label="Second kitchen before renovation" style="background:linear-gradient(180deg,#c9cbcc,#7a7d7e 55%,#2f3130)"></div><span class="ba__tag">Before</span></div>
  <div class="ba" style="left:133px;top:385px"><div class="ba__photo" role="img" aria-label="Second kitchen after renovation with pendant lights and wood island" style="background:linear-gradient(180deg,#f3f3f1,#e3e2dc 55%,#9b7a58)"></div><span class="ba__tag">After</span></div>

  <h2 class="abs head resilient">RESILIENT HOMES BUILT<br>TO ENDURE</h2>
  <div class="abs resilient__copy just">
    <p>In regions like Florida and Colorado, where extreme weather is a constant challenge, Ardson Design Build sets itself apart with its expertise in resilient construction. By focusing on reinforced foundations and materials that exceed building codes, Ardson creates homes that combine energy efficiency, durability, and architectural elegance.</p>
    <p>From hurricane-resistant roofing and moisture-proof materials in Florida to insulated siding and framing designed for Colorado's harsh winters, every detail is thoughtfully engineered to withstand the elements. ArdsonStrong represents the perfect balance of strength, efficiency, and design, ensuring that each home remains a secure and timeless investment.</p>
  </div>

  <svg class="award" style="left:280px;width:56px" viewBox="0 0 56 92"><polygon points="0,0 56,0 56,92 28,82 0,92" fill="var(--ink)"/></svg>
  <svg class="award" style="left:342px;width:56px" viewBox="0 0 56 92"><polygon points="0,0 56,0 56,92 28,82 0,92" fill="var(--ink)"/></svg>
  <svg class="award" style="left:404px;width:59px" viewBox="0 0 59 92"><rect x="0" y="0" width="59" height="92" fill="var(--ink)"/></svg>

  <h2 class="abs head promise">WE BUILD AND SPACES<br>PERFECTLY ALIGNED WITH<br>YOUR UNIQUE VISION.</h2>

  <svg class="abs" style="left:277px;top:550px" width="32" height="18" viewBox="0 0 36 20"><path d="M8 0C3 2 0 6 0 11a7 7 0 1 0 7-7c0-1 1-2 3-3zM26 0c-5 2-8 6-8 11a7 7 0 1 0 7-7c0-1 1-2 3-3z" fill="var(--lime)"/></svg>
  <p class="quote">15 out of 10. It ended up even better that we thought it would. Definitely a higher-end experience.</p>
  <svg class="abs" style="left:426px;top:627px;transform:rotate(180deg)" width="32" height="18" viewBox="0 0 36 20"><path d="M8 0C3 2 0 6 0 11a7 7 0 1 0 7-7c0-1 1-2 3-3zM26 0c-5 2-8 6-8 11a7 7 0 1 0 7-7c0-1 1-2 3-3z" fill="var(--lime)"/></svg>
  <div class="client">
    <div class="client__name">TESSA HOLT</div>
    <div class="client__role">Client, Design Build <span></span></div>
  </div>

  <svg class="abs" style="left:20px;top:606px" width="32" height="34" viewBox="0 0 40 42"><polygon points="20,1 38,11 38,31 20,41 2,31 2,11" fill="var(--lime)"/><rect x="13" y="12" width="14" height="18" rx="2" fill="none" stroke="var(--ink)" stroke-width="2"/><circle cx="20" cy="19" r="2.6" fill="var(--ink)"/><path d="M15.5 26c1.5-3 7.5-3 9 0" stroke="var(--ink)" stroke-width="1.8" fill="none"/></svg>
  <div class="info" style="left:61px;top:603px;color:#fff">
    <div class="info__label" style="font-size:16px">For more info</div>
    <div class="info__phone" style="font-size:20px">555-014-2290</div>
    <div class="info__lic" style="color:var(--lime);margin-left:2px">CGC #1048221</div>
  </div>
  <div class="mail" style="left:21px;top:679px">
    <svg width="11" height="11" viewBox="0 0 12 12"><path d="M11.5 0.5L0.5 5l4 1.5L6 11z" fill="var(--ink)"/></svg>
    hello@ardsonbuild.com
  </div>
</section>

</body>
</html>
```